Metal Warranty card design for Wristwatch brand

I will need a design for a warranty card that will be included with all of our watches. This card will be made from metal and will be rose gold plated. I have attached an example of our current card.

Website with our watch designs: www.pravonwatches.com

Target Market(s)

Men, 20-40s, watch collectors

Requirements
Must have
• Requires these fields and text (follow the example):
• Front:
• www.pravonwatches.com
• Back:
• 1 Year Limited Warranty
• Serial: (signature panel)
• Date: (Signature panel)
• Seller: (large panel)
Nice to have
• Cut outs, watch themed

```html
<!DOCTYPE html>
<html lang="en">
<head>
<meta charset="UTF-8">
<title>Pravon Warranty Card</title>
<link rel="stylesheet" href="https://fonts.googleapis.com/css2?family=Raleway:wght@300;400&display=swap">
<style>
  :root {
    --backdrop: #3b2f29;
    --card: #050505;
    --ink: #ffffff;
    --shadow: rgba(0, 0, 0, 0.55);
  }
  * { margin: 0; padding: 0; box-sizing: border-box; }
  html, body {
    width: 1200px;
    height: 831px;
    overflow: hidden;
    background: var(--backdrop);
    font-family: "Raleway", sans-serif;
    font-variant-numeric: lining-nums;
    color: var(--ink);
  }
  .canvas {
    position: relative;
    width: 1200px;
    height: 831px;
  }
  .card {
    position: absolute;
    top: 245px;
    width: 540px;
    height: 330px;
    background: var(--card);
    border-radius: 6px;
    box-shadow: 0 18px 40px var(--shadow);
  }
  .card--back { left: 45px; }
  .card--front { left: 615px; }

  /* Back side */
  .warranty-title {
    position: absolute;
    top: 36px;
    left: 60px;
    font-size: 21px;
    line-height: 1;
    font-weight: 300;
    letter-spacing: 1px;
  }
  .field-label {
    position: absolute;
    left: 24px;
    font-size: 20px;
    line-height: 20px;
    font-weight: 300;
    letter-spacing: 1px;
  }
  .field-label--serial { top: 84px; }
  .field-label--date { top: 116px; }
  .field-label--seller { top: 148px; }
  .field-panel {
    position: absolute;
    background: var(--ink);
  }
  .field-panel--serial { left: 124px; top: 84px; width: 160px; height: 20px; }
  .field-panel--date { left: 124px; top: 116px; width: 160px; height: 20px; }
  .field-panel--seller { left: 124px; top: 148px; width: 160px; height: 84px; }

  .brand-mark {
    position: absolute;
    border: 3px solid var(--ink);
    border-radius: 50%;
  }
  .card--back .brand-mark { left: 380px; top: 150px; width: 66px; height: 66px; }
  .brand-name {
    position: absolute;
    font-weight: 400;
    letter-spacing: 2px;
    line-height: 1;
  }
  .card--back .brand-name { left: 300px; top: 238px; font-size: 44px; }

  /* Front side */
  .card--front .brand-mark { left: 215px; top: 40px; width: 110px; height: 110px; border-width: 4px; }
  .card--front .brand-name {
    left: 0; right: 0; top: 172px;
    text-align: center;
    font-size: 64px;
  }
  .website {
    position: absolute;
    left: 0; right: 0; top: 264px;
    text-align: center;
    font-size: 19px;
    line-height: 1;
    font-weight: 300;
    letter-spacing: 5px;
  }
</style>
</head>
<body>
<main class="canvas">
  <section class="card card--back" aria-label="Warranty card back">
    <p class="warranty-title">1 YEAR LIMITED WARRANTY</p>
    <span class="field-label field-label--serial">SERIAL</span>
    <span class="field-label field-label--date">DATE</span>
    <span class="field-label field-label--seller">SELLER</span>
    <div class="field-panel field-panel--serial"></div>
    <div class="field-panel field-panel--date"></div>
    <div class="field-panel field-panel--seller"></div>
    <div class="brand-mark"></div>
    <p class="brand-name">PRAVON</p>
  </section>

  <section class="card card--front" aria-label="Warranty card front">
    <div class="brand-mark"></div>
    <p class="brand-name">PRAVON</p>
    <p class="website">www.yourwebsite.com</p>
  </section>
</main>
</body>
</html>
```